Retro Label for old fashioned soda

We need a label for soda we are having private labeled for our retro, 1950's ice cream shop www.thefrostyparlor.net I don't want the label to look like something from 2017 with a retro feel, but more like an original (possibly kinda cheesy) label you'd see from the 1950's with some of the old catch lines like "tastes great", "invigorating" or "it is refreshing!" The prominent brand should be the name of our ice cream shop, The Frosty Parlor. the soda is also pure cane sugar so it might be good to have that on somewhere

Label size is 2.4" wide by 4" tall. Here is an example of some retro labels from lookfindr. I attached on file to this contest but there are more here: https://www.lookfindr.net/results?q=retro+soda+label&id=8Hq2Lm4Pz7Vb1Kc9Xw3Rt6Yd0Ns5Jf2Ga8Ue4Ko1Mi7Bl3Wp9Dv6Qx2Hc5Zr0Ty8Fn4#img=Pk7Rw2Lx9Qm3:

The label will be the same for all the flavors with the exception of the flavor name changing somewhere on the label. These are the flavors

Root Beer
Orange
Black Cherry
Lemonade
Raspberry Lime -Rickey
White Birch Beer
Lemon Iced Tea
Vanilla Cream
Orange Cream
Sarsaparilla
Ginger Ale

• retro feel. authentic old fashioned look

```html
<!DOCTYPE html>
<html lang="en">
<head>
<meta charset="utf-8">
<title>The Frosty Parlor – Vanilla Cream Soda Label</title>
<link rel="stylesheet" href="https://fonts.googleapis.com/css2?family=Leckerli+One&family=Niconne&family=Josefin+Sans:wght@400;700&display=swap">
<style>
  :root {
    --page: #ffffff;
    --cream: #fdf4bc;
    --sun: #fcd77a;
    --parlor-green: #5a9873;
    --ink: #1c1a17;
  }
  html, body {
    margin: 0;
    padding: 0;
    width: 1200px;
    height: 1200px;
    overflow: hidden;
    background: var(--page);
  }
  .canvas {
    position: relative;
    width: 1200px;
    height: 1200px;
  }
  .soda-label {
    position: absolute;
    left: 262px;
    top: 60px;
    width: 675px;
    height: 1080px;
    display: block;
  }
  .tagline {
    font-family: "Niconne", cursive;
    font-size: 46px;
    fill: var(--ink);
  }
  .brand-name {
    font-family: "Leckerli One", cursive;
    font-size: 76px;
    fill: var(--ink);
  }
  .sugar-claim {
    font-family: "Josefin Sans", sans-serif;
    font-weight: 400;
    font-size: 34px;
    fill: var(--ink);
  }
  .flavor-name {
    font-family: "Josefin Sans", sans-serif;
    font-weight: 700;
    font-size: 112px;
    fill: var(--ink);
  }
</style>
</head>
<body>
<main class="canvas">
  <svg class="soda-label" viewBox="0 0 600 960" xmlns="http://www.w3.org/2000/svg" aria-label="Vanilla Cream soda label">
    <defs>
      <radialGradient id="sunburst-tone" cx="50%" cy="72%" r="75%">
        <stop offset="0%" stop-color="#fef7c8"/>
        <stop offset="55%" stop-color="#fbe79c"/>
        <stop offset="100%" stop-color="#fcd77a"/>
      </radialGradient>
    </defs>

    <rect class="label-background" x="0" y="0" width="600" height="960" fill="url(#sunburst-tone)" role="img" aria-label="Radiating sunburst rays in cream and golden yellow"/>

    <rect class="label-frame" x="28" y="27" width="545" height="910" rx="12" fill="none" stroke="var(--parlor-green)" stroke-width="4"/>

    <polygon class="brand-panel" points="40,40 562,40 562,415 40,548" fill="var(--parlor-green)"/>

    <rect class="tagline-box" x="52" y="52" width="496" height="83" fill="var(--cream)"/>
    <text class="tagline" x="300" y="108" text-anchor="middle">it tastes great !</text>

    <text class="brand-name" x="305" y="260" text-anchor="middle">The Frosty</text>
    <text class="brand-name" x="305" y="350" text-anchor="middle">Parlor</text>

    <polygon class="sugar-band" points="50,470 553,354 553,408 50,538" fill="var(--cream)"/>
    <text class="sugar-claim" x="305" y="458" text-anchor="middle" transform="rotate(-13 305 446)">PURE CANE SUGAR</text>

    <text class="flavor-name" x="302" y="676" text-anchor="middle">VANILLA</text>
    <text class="flavor-name" x="302" y="788" text-anchor="middle">CREAM</text>
  </svg>
</main>
</body>
</html>
```